We are a family based professional house keeping and cleaning services company. we offer 30% off for the first cleaning to any new costumer with this post cards, we offer the best service in town 100% guaranteed or money backsome of the services we offer includemove in/out cleaningdeep cleaning in every visitsteam cleaningspecial event cleaningpersonalized cleaning to cover every costumer needs and any requestcontact info phone 513-630-6275email brightnookhelpers42@mailvora.com
middle and upper class
It Company
Designer to choose colors to be used in the design.

```html
<!DOCTYPE html>
<html lang="en">
<head>
<meta charset="utf-8">
<title>Cleaning Services Postcard</title>
<link href="https://fonts.googleapis.com/css2?family=Jost:ital,wght@0,500;0,600;0,700;0,800;1,600;1,700&family=Oswald:wght@500;600&family=Fira+Sans+Condensed:wght@500&family=Arimo:wght@400;700&display=swap" rel="stylesheet">
<style>
  :root {
    --backdrop: #dcdde1;
    --royal: #2f5ea8;
    --navy: #2c4f98;
    --ink-blue: #1f4a8f;
    --sun: #f5dc1e;
    --teal: #1fb5c8;
    --teal-dark: #0f8fa3;
    --bar: #e7ecf5;
    --white: #ffffff;
    --paper: #ffffff;
    --mail-ink: #111111;
  }
  * { margin: 0; padding: 0; box-sizing: border-box; }
  html, body { width: 1200px; height: 1200px; overflow: hidden; background: var(--backdrop); }

  .postcard {
    position: absolute;
    left: 120px;
    width: 1200px;
    height: 667px;
    transform: scale(0.8);
    transform-origin: top left;
    overflow: hidden;
    background: var(--paper);
  }
  .postcard--front { top: 36px; }
  .postcard--back { top: 600px; }

  /* FRONT */
  .family-photo {
    position: absolute; left: 0; top: 0; width: 760px; height: 667px;
    background: linear-gradient(135deg, #eef0ec 0%, #d9dcd6 35%, #c9a98f 60%, #a8c2dd 85%);
  }
  .blue-panel { position: absolute; inset: 0; width: 1200px; height: 667px; }
  .headline {
    position: absolute; left: 490px; top: 70px; width: 670px; height: 70px; overflow: visible;
  }
  .headline text {
    font: 800 60px/1 "Jost", sans-serif; fill: var(--white);
  }
  .tagline {
    position: absolute; left: 494px; top: 142px; width: 585px;
    font: italic 700 25px/29px "Jost", sans-serif; color: var(--white);
  }
  .service-list { position: absolute; left: 600px; top: 229px; list-style: none; }
  .service-list li {
    display: flex; align-items: center; gap: 12px; height: 38.5px; white-space: nowrap;
    font: 600 22px/1 "Jost", sans-serif; color: var(--white);
  }
  .service-list svg { width: 26px; height: 26px; flex: none; }

  .discount-badge { position: absolute; left: 586px; top: 405px; width: 270px; height: 165px; }
  .discount-word {
    position: absolute; left: 620px; top: 448px;
    font: 600 38px/1 "Oswald", sans-serif; color: var(--ink-blue); transform: scaleX(0.85); transform-origin: left;
  }
  .discount-note {
    position: absolute; left: 624px; top: 496px; white-space: nowrap;
    font: 500 16px/1 "Jost", sans-serif; color: var(--teal-dark); letter-spacing: 0.3px;
  }
  .discount-rate {
    position: absolute; left: 757px; top: 425px; width: 76px; text-align: center;
    font: 500 33px/1 "Oswald", sans-serif; color: var(--white);
  }
  .offer-copy {
    position: absolute; left: 865px; top: 456px; width: 295px;
    font: italic 700 18.5px/22px "Jost", sans-serif; color: var(--white);
  }

  .contact-bar {
    position: absolute; left: 0; top: 560px; width: 1200px; height: 70px;
    background: var(--bar);
  }
  .contact-item {
    position: absolute; top: 0; height: 70px; display: flex; align-items: center; gap: 30px; white-space: nowrap;
    font: 500 31px/1 "Fira Sans Condensed", sans-serif; color: var(--royal);
  }
  .contact-item--phone { left: 105px; }
  .contact-item--email { left: 520px; font-size: 34px; }
  .contact-item svg { flex: none; }

  /* BACK */
  .interior-photo {
    position: absolute; left: 0; top: 0; width: 776px; height: 667px;
    background: linear-gradient(180deg, #f4f5f6 0%, #eceef0 50%, #e6d8c2 75%, #ead9bf 100%);
    opacity: 0.95;
  }
  .back-title {
    position: absolute; left: 88px; top: 135px; white-space: nowrap;
    font: 700 38px/43px "Jost", sans-serif; color: var(--navy); letter-spacing: 0.4px;
  }
  .guarantee {
    position: absolute; left: 90px; top: 258px; white-space: nowrap;
    font: 700 28px/1 "Jost", sans-serif; color: var(--navy);
  }
  .booking { position: absolute; left: 88px; top: 426px; white-space: nowrap; }
  .booking p {
    font: 700 21px/35.5px "Jost", sans-serif; color: var(--navy); text-transform: uppercase;
  }
  .postage-indicia {
    position: absolute; left: 1005px; top: 87px; width: 81px; height: 80px;
    border: 1px solid var(--mail-ink); text-align: center; padding-top: 6px;
    font: 400 10.5px/13px "Arimo", sans-serif; color: var(--mail-ink);
  }
  .postage-indicia b { font-weight: 700; }
  .address-block {
    position: absolute; left: 819px; top: 418px; width: 267px; height: 107px;
    border: 1px solid var(--mail-ink); font: 400 15px/16px "Arimo", sans-serif; color: var(--mail-ink);
  }
  .address-block .route { position: absolute; right: 20px; top: 14px; font-size: 12px; }
  .address-block .recipient { position: absolute; left: 19px; top: 52px; }
</style>
</head>
<body>

<section class="postcard postcard--front">
  <div class="family-photo" role="img" aria-label="Smiling family of three in a bright home with a window behind them"></div>
  <svg class="blue-panel" viewBox="0 0 1200 667" aria-hidden="true">
    <path d="M512,0 C430,150 420,380 560,667 L1200,667 L1200,0 Z" fill="#2f5ea8"/>
  </svg>

  <svg class="headline" viewBox="0 0 670 70" role="heading" aria-level="1">
    <text x="3" y="55" textLength="652" lengthAdjust="spacingAndGlyphs">WE CLEAN, YOU RELAX!</text>
  </svg>
  <p class="tagline">Family based professional house keeping and cleaning services that you can trust.</p>

  <ul class="service-list">
    <li><svg viewBox="0 0 26 26"><circle cx="13" cy="13" r="10.5" fill="none" stroke="#f5dc1e" stroke-width="2.6"/><path d="M7.5 13.5 L12 17.5 L21 6" fill="none" stroke="#f5dc1e" stroke-width="3" stroke-linecap="round" stroke-linejoin="round"/></svg>Move in/out cleaning</li>
    <li><svg viewBox="0 0 26 26"><circle cx="13" cy="13" r="10.5" fill="none" stroke="#f5dc1e" stroke-width="2.6"/><path d="M7.5 13.5 L12 17.5 L21 6" fill="none" stroke="#f5dc1e" stroke-width="3" stroke-linecap="round" stroke-linejoin="round"/></svg>Deep cleaning in every visit</li>
    <li><svg viewBox="0 0 26 26"><circle cx="13" cy="13" r="10.5" fill="none" stroke="#f5dc1e" stroke-width="2.6"/><path d="M7.5 13.5 L12 17.5 L21 6" fill="none" stroke="#f5dc1e" stroke-width="3" stroke-linecap="round" stroke-linejoin="round"/></svg>Special event cleaning</li>
    <li><svg viewBox="0 0 26 26"><circle cx="13" cy="13" r="10.5" fill="none" stroke="#f5dc1e" stroke-width="2.6"/><path d="M7.5 13.5 L12 17.5 L21 6" fill="none" stroke="#f5dc1e" stroke-width="3" stroke-linecap="round" stroke-linejoin="round"/></svg>Personalized cleaning covering costumer needs</li>
  </ul>

  <svg class="discount-badge" viewBox="0 0 270 165" aria-hidden="true">
    <polygon points="126,117 170,117 128,160" fill="#1fa9bb"/>
    <polygon points="2,23 264,23 264,117 16,117" fill="#f5dc1e"/>
    <circle cx="209" cy="40" r="39" fill="#2f5ea8"/>
    <circle cx="209" cy="40" r="36" fill="#1fb5c8"/>
  </svg>
  <div class="discount-word">DISCOUNT</div>
  <div class="discount-note">FOR THE FIRST CLEANING</div>
  <div class="discount-rate">30%</div>
  <p class="offer-copy">We offer 30% off for the first cleaning to any new costumer with this post cards.</p>

  <div class="contact-bar">
    <div class="contact-item contact-item--phone">
      <svg width="44" height="32" viewBox="0 0 44 32" aria-hidden="true">
        <path d="M2 12 C2 2 42 2 42 12 L42 15 L32 15 L32 10 L12 10 L12 15 L2 15 Z" fill="#1fb5c8"/>
        <path d="M9 16 L14 12 L30 12 L35 16 L38 30 L6 30 Z" fill="#1fb5c8"/>
        <circle cx="22" cy="21" r="5" fill="#e7ecf5"/>
        <circle cx="22" cy="21" r="2.2" fill="#1fb5c8"/>
      </svg>
      <span>555-284-9137</span>
    </div>
    <div class="contact-item contact-item--email">
      <svg width="36" height="32" viewBox="0 0 36 32" aria-hidden="true">
        <path d="M0 12 L18 0 L36 12 L36 32 L0 32 Z" fill="#1fb5c8"/>
        <text x="18" y="27" text-anchor="middle" font-family="Arimo, sans-serif" font-size="14" fill="#e7ecf5">@</text>
      </svg>
      <span>brightnookhelpers42@mailvora.com</span>
    </div>
  </div>
</section>

<section class="postcard postcard--back">
  <div class="interior-photo" role="img" aria-label="Bright, airy living room with white walls and light wooden floor"></div>
  <h2 class="back-title">WE OFFER THE BEST<br>SERVICE IN TOWN</h2>
  <p class="guarantee">100% guaranteed or money back!</p>
  <div class="booking">
    <p>For booking please contact</p>
    <p>Phone:555-284-9137</p>
    <p>Email: brightnookhelpers42@mailvora.com</p>
  </div>

  <div class="postage-indicia">PRSRT STD<br>ECRWSS<br>U.S. Postage<br><b>PAID</b><br>EDDM RETAIL</div>
  <div class="address-block">
    <span class="route">****************ECRWSS****</span>
    <span class="recipient">Local<br>Postal Customer</span>
  </div>
</section>

</body>
</html>
```